Tildens Biscuit Barn Website

I need a website for a diner/restaurant that has been established in a farming, oil and industrial community for over 15 years. The website needs to be simple in design, but that should demonstrate the mastery of skills of the designer. Our diner/restaurant is family oriented, patriotic but very rustic
Fb Address is fb.me/TildensBarn

Pictures of the restaurant

https://www.filecrate-example.net/s/qk72hdw01/Tildens_05.jpg

Pictures of About us

https://www.filecrate-example.net/sh/zm40vrt88/AboutUsPhotos

Article about Tilden's
https://www.filecrate-example.net/s/wp31nbx57/TildensBiscuitBarn1.PDF
https://www.filecrate-example.net/s/hy65lcu29/TildensBiscuitBarn2.PDF

Reason: I was slow to update with information.

Reason: I am just getting feedback to the designs posted. I wasn't sure of the limited feedback was limiting designers from submitting designs. That and running a business with 25 employees open 12 hours a day, being here 2 hours prior and 2-3 hours after makes for long days.

I've increased the first place prize and also added funds to the second and third place prizes for your effort.

I just need the files in PSD, not HTML 5 as originally requested. We can handle getting the coding part.

Ill have the contest finalized by Monday. Thanks for your patience.

Target Market(s)

Cross section of adults from 18-35 & 35-55.

Industry/Entity Type

Industrial

Font styles to use
Other font styles liked:
• ff tisa web pro or garamond premier pro

Requirements
Must have
• Must be clean, look nice and not look like an afterthought.
Nice to have
• Please see the last two documents for information about our restaurant, which was featured in our local newspaper.

```html
<!DOCTYPE html>
<html lang="en">
<head>
<meta charset="utf-8">
<title>Tildens Biscuit Barn</title>
<link href="https://fonts.googleapis.com/css2?family=Architects+Daughter&family=Josefin+Sans:wght@400&family=Teko:wght@500&display=swap" rel="stylesheet">
<style>
:root{
  --board:#2c2c2c;
  --board-edge:#222;
  --chalk:#ededed;
  --chalk-soft:#cfcfcf;
  --paper:#e6e6e6;
  --paper-edge:#d8d8d8;
  --ink:#3a3a3a;
  --frame:#5a5a5a;
  --map:#dedbd3;
}
*{margin:0;padding:0;box-sizing:border-box}
html,body{width:1200px;height:1154px;overflow:hidden}
body{position:relative;background:var(--paper)}
.chalkboard{position:absolute;left:0;top:0;width:1200px;height:710px;
  background:radial-gradient(ellipse at 50% 40%,#353535 0%,var(--board) 55%,var(--board-edge) 100%);
  font-family:"Architects Daughter",cursive;color:var(--chalk);text-transform:uppercase}
.dish,.note,.price{position:absolute;white-space:nowrap}
.dish{font-size:22px;line-height:30px;letter-spacing:.4px}
.dish small{font-size:13px;letter-spacing:.3px;color:var(--chalk-soft)}
.note{font-size:13px;line-height:22px;color:var(--chalk-soft);letter-spacing:.3px}
.price{font-size:27px;line-height:34px;text-align:right;width:160px}
.left .dish,.left .note{left:91px}
.left .price{left:412px}
.right .dish,.right .note{left:607px}
.right .price{left:930px}
.lunch-link{position:absolute;left:410px;top:623px;font-family:"Josefin Sans",sans-serif;font-size:22px;letter-spacing:2px;line-height:34px;white-space:nowrap}
.lunch-arrow{position:absolute;left:790px;top:595px}
.footer{position:absolute;left:0;top:710px;width:1200px;height:444px;
  background:linear-gradient(180deg,var(--paper) 0%,var(--paper-edge) 100%);
  font-family:"Teko",sans-serif;color:var(--ink);text-transform:uppercase}
.map-frame{position:absolute;left:48px;top:50px;width:362px;height:340px;background:var(--frame);
  box-shadow:3px 4px 6px rgba(0,0,0,.35);padding:42px 44px}
.map{width:100%;height:100%;background:linear-gradient(160deg,#e9e7e1,var(--map))}
.icon{position:absolute}
.info{position:absolute;left:559px;font-size:30px;line-height:40px;letter-spacing:2px;white-space:nowrap}
.copyright{position:absolute;left:468px;top:371px;font-size:15px;letter-spacing:1px}
.likes{position:absolute;left:918px;top:362px;font-size:26px;letter-spacing:.5px;white-space:nowrap}
.likes-dot{position:absolute;left:1030px;top:352px;width:50px;height:50px;border:3px solid var(--ink);border-radius:50%}
</style>
</head>
<body>
<section class="chalkboard">
  <div class="left">
    <div class="note" style="top:-6px">Served with two eggs</div>
    <div class="dish" style="top:24px">Chicken Fried Steak</div>
    <div class="note" style="top:56px">(One of the biggest in town) with two eggs</div>
    <div class="price" style="top:23px">Full-11.29</div>
    <div class="price" style="top:60px">Half-8.99</div>

    <div class="dish" style="top:98px">Jumbo Ham Steak</div>
    <div class="note" style="top:129px">(One of the biggest in town) with two eggs</div>
    <div class="price" style="top:98px">11.29</div>

    <div class="dish" style="top:159px">Steak and Eggs</div>
    <div class="note" style="top:189px">USDA prime 10oz rib-eye with two eggs. Get 'em cowboy</div>
    <div class="price" style="top:158px">11.29</div>

    <div class="dish" style="top:219px">All-American Breakfast</div>
    <div class="note" style="top:249px">Two eggs with 4 bacon or 2 sausage</div>
    <div class="price" style="top:218px">8.79</div>

    <div class="note" style="top:287px">One egg with 2 bacon or 1 sausage</div>
    <div class="price" style="top:280px">6.99</div>

    <div class="dish" style="top:317px">Corned Beef Hash <small>with two eggs</small></div>
    <div class="price" style="top:316px">8.99</div>

    <div class="dish" style="top:354px">Migas</div>
    <div class="note" style="top:384px">Three corn tortillas fried until golden brown</div>
    <div class="note" style="top:407px">and scrambled with two eggs</div>
    <div class="price" style="top:353px">8.99</div>

    <div class="dish" style="top:436px">Deluxe Scramble</div>
    <div class="note" style="top:467px">Ham, Mesa chiles, onions and cheese</div>
    <div class="price" style="top:436px">8.99</div>

    <div class="dish" style="top:497px">Meat Lovers Skillet</div>
    <div class="note" style="top:527px">Hot links, ham, sausage, bacon and jack cheese</div>
    <div class="price" style="top:497px">9.79</div>
  </div>

  <div class="right">
    <div class="dish" style="top:1px">Denver Omelet</div>
    <div class="note" style="top:31px">Ham, onions, bell peppers and cheese</div>
    <div class="price" style="top:0px">9.69</div>

    <div class="dish" style="top:62px">Broccoli Omelet</div>
    <div class="note" style="top:92px">Broccoli, ham, mushrooms and jack cheese</div>
    <div class="price" style="top:61px">9.79</div>

    <div class="dish" style="top:123px">Cowboy Benedict</div>
    <div class="note" style="top:152px">Two sausage patties on an open biscuit,</div>
    <div class="note" style="top:174px">two poached eggs and gravy</div>
    <div class="price" style="top:122px">9.79</div>

    <div class="dish" style="top:205px">Cheese Omelet</div>
    <div class="price" style="top:204px">8.99</div>

    <div class="dish" style="top:243px">Ham and Cheese Omelet</div>
    <div class="price" style="top:242px">9.79</div>

    <div class="dish" style="top:281px">Monterey Omelet</div>
    <div class="note" style="top:310px">Mesa chilies, ham and jack cheese</div>
    <div class="price" style="top:280px">9.79</div>

    <div class="dish" style="top:341px">Snake Bite Omelet</div>
    <div class="note" style="top:370px">Polish sausage, pickled jalapenos,</div>
    <div class="note" style="top:392px">yellow pepper rings and jack cheese</div>
    <div class="price" style="top:340px">10.19</div>

    <div class="dish" style="top:423px">Hobo Omelet</div>
    <div class="note" style="top:453px">Bacon, ham, sausage, onions, tomatoes, bell peppers,</div>
    <div class="note" style="top:475px">mushrooms and cheese</div>
    <div class="price" style="top:422px">10.49</div>

    <div class="dish" style="top:506px">Harvest Omelet</div>
    <div class="note" style="top:535px">Sausage, bell peppers, onions and cheese</div>
    <div class="price" style="top:505px">9.79</div>
  </div>

  <div class="lunch-link">Tilden's Hearty Lunches</div>
  <svg class="lunch-arrow" width="92" height="66" viewBox="0 0 92 66" aria-hidden="true">
    <path d="M6 33 H70 M50 13 L72 33 L50 53" fill="none" stroke="var(--chalk)" stroke-width="4" stroke-linecap="round" stroke-linejoin="round"/>
  </svg>
</section>

<footer class="footer">
  <div class="map-frame">
    <div class="map" role="img" aria-label="Street map showing the location of Tildens Biscuit Barn"></div>
  </div>

  <svg class="icon" style="left:461px;top:61px" width="68" height="68" viewBox="0 0 68 68" aria-hidden="true">
    <circle cx="34" cy="34" r="29" fill="none" stroke="var(--ink)" stroke-width="5"/>
    <path d="M34 16 V35 H48" fill="none" stroke="var(--ink)" stroke-width="5" stroke-linecap="round"/>
  </svg>
  <div class="info" style="top:64px">An All-American Coffee Shop<br>Open 5:30AM-2:00PM Daily</div>

  <svg class="icon" style="left:459px;top:165px" width="80" height="92" viewBox="0 0 80 92" aria-hidden="true">
    <path d="M40 70 C28 52 18 42 18 28 A22 22 0 0 1 62 28 C62 42 52 52 40 70 Z" fill="none" stroke="var(--ink)" stroke-width="5"/>
    <circle cx="40" cy="28" r="9" fill="none" stroke="var(--ink)" stroke-width="5"/>
    <path d="M22 62 L4 88 H76 L58 62" fill="none" stroke="var(--ink)" stroke-width="4" stroke-linejoin="round"/>
  </svg>
  <div class="info" style="top:184px">4820 Cottonwood Highway,<br>Millbrook, CA 93390</div>

  <div class="copyright">2014 © All Rights Reserved</div>
  <div class="likes">6,439 Likes</div>
  <div class="likes-dot"></div>
</footer>
</body>
</html>
```